KOVlane stands for Kestrel & Ordway venture technologies and specialises in process automation

We are a New company called KOVlane (Kestrel & Ordway venture technologies) a Brisbane based company speciallising in Process Automation for the oil and Gas industry in Australia. We work on projects for DCS, RTU and PLC automation this involves programming and commissioning. We initially need a Website that customers can see about the company and make enquiries. We currently have Royal Blue and grey as our colours on our email signatures but are open for suggestions. Keywords i would suggest yo to look at for insperation are CSG ( coalseam gas) DCS (Distributed control system) RTU (remote terminal unit) and PLC (programmable logic controller).

Target Market(s)

Large CSG companies in Australia, Marlow, Telmar, WXJ, Bendle

Industry/Entity Type

Industry

```html
<!DOCTYPE html>
<html lang="en">
<head>
<meta charset="utf-8">
<title>KOVlane — Kestrel & Ordway venture technologies</title>
<link href="https://fonts.googleapis.com/css2?family=PT+Sans:wght@400;700&family=PT+Sans+Narrow:wght@400;700&display=swap" rel="stylesheet">
<style>
:root{
  --royal:#233a8f;
  --royal-deep:#1c2a7e;
  --navy-bg:#1d2a86;
  --sky-bg:#1f7fc4;
  --link-blue:#1b5fa8;
  --teal-btn:#1a8bc9;
  --red:#d11a1a;
  --grey-text:#555;
  --light-line:#dcdcdc;
  --footer:#0d0d0f;
  --social:#1f5fa8;
  --white:#fff;
}
*{box-sizing:border-box;margin:0;padding:0}
html,body{width:965px;height:1200px;overflow:hidden}
body{position:relative;font-family:"PT Sans",sans-serif;color:var(--grey-text);
  background:linear-gradient(180deg,var(--navy-bg) 0%,#1f4fa3 45%,var(--sky-bg) 100%)}
.abs{position:absolute}
.page{position:absolute;left:76px;top:40px;width:823px;height:1037px;background:var(--white)}
.brand{left:32px;top:14px;font-size:30px;font-weight:700;color:var(--royal);letter-spacing:.3px}
.tagline{left:32px;top:52px;font-size:14px;color:#444}
.search{left:565px;top:44px;width:206px;height:26px;border:1px solid var(--light-line);font-size:10px;font-style:italic;color:#888;padding:6px 18px}
.search-btn{left:771px;top:44px;width:31px;height:26px;background:#3b6fc0}
.nav{left:0;top:85px;width:823px;height:37px;border-top:1px solid var(--light-line);background:linear-gradient(#fff,#f0f0f0);font-family:"PT Sans Narrow",sans-serif;font-size:13px;color:#555}
.nav-item{position:absolute;top:0;height:36px;line-height:36px;text-align:center;border-right:1px solid var(--light-line)}
.nav-item.active{background:var(--royal);color:#fff}
.hero{left:0;top:133px;width:823px;height:345px;background:var(--royal-deep)}
.hero-title{left:557px;top:64px;width:254px;height:28px;background:#fff;border-radius:3px;font-family:"PT Sans Narrow",sans-serif;font-size:16px;color:var(--royal);text-align:center;line-height:28px}
.hero-text{left:562px;top:108px;width:244px;font-size:10.6px;line-height:17px;color:#dde3f5;text-align:justify}
.hero-btn{left:568px;top:227px;width:108px;height:29px;background:#14205a;border-radius:3px;color:#fff;font-family:"PT Sans Narrow",sans-serif;font-weight:700;font-size:13px;text-align:center;line-height:29px}
.dot{top:284px;width:8px;height:8px;border-radius:50%;background:#111}
.section-title{left:0;top:497px;width:823px;text-align:center;font-family:"PT Sans Narrow",sans-serif;font-weight:700;font-size:21px;color:var(--royal)}
.section-rule{top:508px;height:1px;background:var(--light-line)}
.service{top:542px;width:176px}
.service h3{font-weight:400;font-size:12.5px;color:var(--royal);white-space:nowrap;letter-spacing:-.2px}
.service h3 b{font-weight:400;font-size:15px}
.service .thumb{margin-top:7px;width:176px;height:89px;border-radius:3px}
.service p{margin-top:8px;font-size:8.6px;line-height:12.9px;text-align:justify}
.service .more{margin-top:9px;font-size:9.5px;color:var(--red)}
.welcome{left:18px;top:818px;font-size:15.5px;font-weight:400;color:#222}
.welcome-rule{left:18px;top:843px;width:553px;height:1px;background:var(--light-line)}
.welcome-sub{left:18px;top:854px;font-size:12px;color:var(--link-blue)}
.welcome-text{left:18px;width:553px;font-size:8.5px;line-height:14.5px;color:#444}
.learn-btn{left:509px;top:986px;width:65px;height:25px;background:var(--teal-btn);color:#fff;font-size:10px;text-align:center;line-height:25px}
.news{left:599px;top:819px;width:208px;height:194px;border:1px solid #d0d0d0;border-radius:4px;background:linear-gradient(#fff,#f4f4f4);box-shadow:0 4px 6px -4px #999}
.news h4{position:absolute;left:50px;top:12px;font-weight:400;font-size:15.5px;color:var(--link-blue)}
.news .rule{position:absolute;left:10px;top:38px;width:188px;height:1px;background:var(--light-line)}
.news p{position:absolute;left:14px;top:46px;width:185px;font-size:8.3px;line-height:17px}
.field{position:absolute;left:11px;width:186px;height:21px;border:1px solid #ccc;background:#fff;font-size:8.5px;color:#666;padding:4px 8px}
.subscribe{position:absolute;left:108px;top:152px;width:89px;height:27px;border-radius:6px;background:linear-gradient(#2a6fb5,#164f8e);color:#fff;font-size:12px;font-weight:700;text-align:center;line-height:27px}
.footer{left:0;top:1107px;width:965px;height:93px;background:var(--footer);color:#ddd}
.connect{left:80px;top:16px;font-size:14px}
.social{top:50px;width:25px;height:25px}
.legal{right:72px;font-size:8.5px;color:#ccc;text-align:right}
</style>
</head>
<body>
<div class="page">
  <div class="abs brand">KOVlane</div>
  <div class="abs tagline">Kestrel &amp; Ordway venture technologies.</div>
  <div class="abs search">Search</div>
  <div class="abs search-btn">
    <svg width="31" height="26" viewBox="0 0 31 26"><circle cx="14.5" cy="12" r="5" fill="none" stroke="#fff" stroke-width="2.2"/><line x1="18" y1="15.5" x2="21.5" y2="19" stroke="#fff" stroke-width="2.5" stroke-linecap="round"/></svg>
  </div>

  <nav class="abs nav">
    <div class="nav-item active" style="left:0;width:97px">HOME</div>
    <div class="nav-item" style="left:97px;width:93px">ABOUT US</div>
    <div class="nav-item" style="left:190px;width:91px">PRODUCTS</div>
    <div class="nav-item" style="left:281px;width:82px">SERVICES</div>
    <div class="nav-item" style="left:363px;width:119px">TESTIMONIALS</div>
    <div class="nav-item" style="left:482px;width:100px;border:none">CONTACT US</div>
  </nav>

  <section class="abs hero">
    <svg class="abs" style="left:0;top:0" width="823" height="345" viewBox="0 0 823 345" role="img" aria-label="Engineer in safety glasses inspecting a wired automation control cabinet with a laptop">
      <defs><linearGradient id="heroPhoto" x1="0" x2="1"><stop offset="0" stop-color="#8c8f93"/><stop offset=".55" stop-color="#b7b8b6"/><stop offset="1" stop-color="#6f7a88"/></linearGradient></defs>
      <path d="M0 0 H540 C600 20 640 60 605 180 C580 260 560 310 520 345 H0 Z" fill="url(#heroPhoto)"/>
    </svg>
    <div class="abs hero-title">PROCESS &amp; AUTOMATION SYSTEM</div>
    <p class="abs hero-text">Sed ut perspiciatis unde omnis iste natus error sit voluptatem accusantium doloremque laudantium, totam rem aperiam, eaque ipsa quae ab illo inventore veritatis et quasi architecto beatae vitae dicta sunt explicabo. Nemo enim ipsam voluptatem quia voluptas sit aspernatur aut odit aut fugit</p>
    <div class="abs hero-btn">LEARN MORE</div>
    <span class="abs dot" style="left:583px;background:#2ea3f2"></span>
    <span class="abs dot" style="left:595px"></span>
    <span class="abs dot" style="left:607px"></span>
    <span class="abs dot" style="left:619px"></span>
  </section>

  <div class="abs section-rule" style="left:0;width:360px"></div>
  <div class="abs section-rule" style="left:483px;width:340px"></div>
  <h2 class="abs section-title">Our Services</h2>

  <div class="abs service" style="left:17px">
    <h3><b>CSG</b> (Coalseam Gas)</h3>
    <div class="thumb" role="img" aria-label="Worker beside a large gas pipeline at a coal seam gas plant" style="background:linear-gradient(180deg,#2b6fc4,#8bb4de 55%,#9a8a70)"></div>
    <p>Sed ut perspiciatis unde omnis iste natus voluptatem accusantium doloremque laudantium, totam rem aperiam, eaque ipsa quae ab illo inventore veritatis et quasi. eaque ipsa quae ab illo inventore veritatis et quasi.</p>
    <div class="more">VIEW MORE ▸</div>
  </div>
  <div class="abs service" style="left:219px">
    <h3><b>DCS</b> (Distributed Control System)</h3>
    <div class="thumb" role="img" aria-label="Control room with operator desks and monitor screens" style="background:linear-gradient(180deg,#c9ccd0,#eef0f2)"></div>
    <p>Sed ut perspiciatis unde omnis iste natus voluptatem accusantium doloremque laudantium, totam rem aperiam, eaque ipsa quae ab illo inventore veritatis et quasi. eaque ipsa quae ab illo inventore veritatis et quasi.</p>
    <div class="more">VIEW MORE ▸</div>
  </div>
  <div class="abs service" style="left:421px">
    <h3><b>RTU</b> (Remote Terminal Unit)</h3>
    <div class="thumb" role="img" aria-label="Row of blue remote terminal unit modules" style="background:linear-gradient(180deg,#1d3f8c,#142a5e)"></div>
    <p>Sed ut perspiciatis unde omnis iste natus voluptatem accusantium doloremque laudantium, totam rem aperiam, eaque ipsa quae ab illo inventore veritatis et quasi. eaque ipsa quae ab illo inventore veritatis et quasi.</p>
    <div class="more">VIEW MORE ▸</div>
  </div>
  <div class="abs service" style="left:623px">
    <h3><b>PLC</b> (Programmable Logic Controller)</h3>
    <div class="thumb" role="img" aria-label="Technician operating a programmable logic controller panel" style="background:linear-gradient(90deg,#7d8187,#a9a9a6 60%,#d8d2c8)"></div>
    <p>Sed ut perspiciatis unde omnis iste natus voluptatem accusantium doloremque laudantium, totam rem aperiam, eaque ipsa quae ab illo inventore veritatis et quasi. eaque ipsa quae ab illo inventore veritatis et quasi.</p>
    <div class="more">VIEW MORE ▸</div>
  </div>

  <h2 class="abs welcome">Welcome to Kestrel &amp; Ordway Venture Technologies</h2>
  <div class="abs welcome-rule"></div>
  <div class="abs welcome-sub">Mauris vel lacus vitae felis vestibulum volutpat. Etiam est nunc, venisl.</div>
  <p class="abs welcome-text" style="top:880px">Sed ut perspiciatis unde omnis iste natus error sit voluptatem accusantium doloremque laudantium, totam rem aperiam, eaque ipsa quae ab illo inventore veritatis et quasi architecto beatae vitae dicta sunt explicabo. Nemo enim ipsam voluptatem quia voluptas sit aspernatur aut odit aut fugit, sed quia consequuntur magni dolores eos qui ratione voluptatem sequi nesciunt.</p>
  <p class="abs welcome-text" style="top:931px">Sed ut perspiciatis unde omnis iste natus error sit voluptatem accusantium doloremque laudantium, totam rem aperiam, eaque ipsa quae ab illo inventore veritatis et quasi architecto beatae vitae dicta sunt explicabo. Nemo enim ipsam voluptatem quia voluptas sit aspernatur aut odit aut fugit, sed quia consequuntur magni dolores eos qui ratione voluptatem sequi nesciunt. Neque porro quisquam est, qui dolorem ipsum quia dolor sit amet.</p>
  <div class="abs learn-btn">Learn More</div>

  <aside class="abs news">
    <svg style="position:absolute;left:16px;top:10px" width="26" height="22" viewBox="0 0 26 22"><rect x="1" y="7" width="24" height="14" rx="1" fill="#e8edf5" stroke="#7a93c0"/><path d="M1 7 L13 1 L25 7" fill="#f4c23a" stroke="#c9961a"/><path d="M1 8 L13 15 L25 8" fill="none" stroke="#7a93c0"/></svg>
    <h4>Newsletter</h4>
    <div class="rule"></div>
    <p>Sed ut perspiciatis unde omnis iste natus error sit voluptatem accusantium doloremque</p>
    <div class="field" style="top:89px">Name</div>
    <div class="field" style="top:120px">Email</div>
    <div class="subscribe">Subscribe</div>
  </aside>
</div>

<footer class="abs footer">
  <div class="abs connect">Connect With Us</div>
  <svg class="abs social" style="left:79px" viewBox="0 0 25 25" aria-label="Social link"><circle cx="12.5" cy="12.5" r="11.5" fill="var(--social)" stroke="#fff" stroke-width="1.5"/><path d="M9 12.5h7M13 9.5l3 3-3 3" fill="none" stroke="#fff" stroke-width="1.6" stroke-linecap="round"/></svg>
  <svg class="abs social" style="left:107px" viewBox="0 0 25 25" aria-label="Social link"><circle cx="12.5" cy="12.5" r="11.5" fill="#111" stroke="#fff" stroke-width="1.5"/><path d="M9 12.5h7M13 9.5l3 3-3 3" fill="none" stroke="#fff" stroke-width="1.6" stroke-linecap="round"/></svg>
  <svg class="abs social" style="left:135px" viewBox="0 0 25 25" aria-label="Social link"><circle cx="12.5" cy="12.5" r="11.5" fill="#111" stroke="#fff" stroke-width="1.5"/><path d="M9 12.5h7M13 9.5l3 3-3 3" fill="none" stroke="#fff" stroke-width="1.6" stroke-linecap="round"/></svg>
  <svg class="abs social" style="left:163px" viewBox="0 0 25 25" aria-label="Social link"><circle cx="12.5" cy="12.5" r="11.5" fill="#111" stroke="#fff" stroke-width="1.5"/><path d="M9 12.5h7M13 9.5l3 3-3 3" fill="none" stroke="#fff" stroke-width="1.6" stroke-linecap="round"/></svg>
  <svg class="abs social" style="left:191px" viewBox="0 0 25 25" aria-label="Social link"><circle cx="12.5" cy="12.5" r="11.5" fill="#111" stroke="#fff" stroke-width="1.5"/><path d="M9 12.5h7M13 9.5l3 3-3 3" fill="none" stroke="#fff" stroke-width="1.6" stroke-linecap="round"/></svg>
  <svg class="abs social" style="left:220px" viewBox="0 0 25 25" aria-label="Social link"><circle cx="12.5" cy="12.5" r="11.5" fill="#111" stroke="#fff" stroke-width="1.5"/><path d="M9 12.5h7M13 9.5l3 3-3 3" fill="none" stroke="#fff" stroke-width="1.6" stroke-linecap="round"/></svg>
  <div class="abs legal" style="top:26px">Privacy Policy | Terms of Use | &nbsp;Contact</div>
  <div class="abs legal" style="top:43px">© 2013 .KOVlane , All Rights Reserved</div>
</footer>
</body>
</html>
```